Personal Home Page

I'm an independent film maker that recently graduated with a master's in film making, I have done many short films and won awards, I have worked on many other film projects.
I like to have a single home page that's interactive, think crazy, funny, weired is very much welcome (rex hadley kinda) the sole purpose of this page is to promote myself and what I do very briefly with contact details, in a way if anyone goes to the site gets drown in and has fun viewing or experiencing it ! I love the magic designers bring to the table, I'm very open for any creative inputs, thanks
Here are just some examples of what I mean by interactive or entertaining :
http://www.plumreels.com.sg/
http://www.brisklane.com/
Reason: the designs submitted didn't meet the requirements in the brief
Target Market(s)
movie lovers, younger generation, art lovers, media production proffesionals
Requirements
Must have
- contact details, just an email would be enough !
Nice to have
- things relate to movie making, camera, film rolling...etc. but it's not a must
Should not have
- adult material, frightening elements (sudden loud scream or so)
A template that I can get for free online or build on qorv.com

```html
<!DOCTYPE html>
<html lang="en">
<head>
<meta charset="utf-8">
<title>Karim · Independent Film Maker</title>
<link href="https://fonts.googleapis.com/css2?family=Oswald:wght@400;700&family=Comfortaa:wght@400&family=Black+Ops+One&family=Nothing+You+Could+Do&family=Arimo&display=swap" rel="stylesheet">
<style>
:root{
  --topbar:#3a2a05;
  --hero:#6f5009;
  --hero-dark:#4f3906;
  --gold:#f6b90a;
  --orange:#f29a12;
  --cream:#f4efe3;
  --denim:#1c1c1c;
  --footer:#050505;
  --muted:#8c8c8c;
}
*{margin:0;padding:0;box-sizing:border-box}
html,body{width:1200px;height:750px;overflow:hidden;background:var(--footer)}
.page{position:relative;width:1200px;height:750px;overflow:hidden}
.topbar{position:absolute;left:0;top:0;width:1200px;height:14px;background:var(--topbar)}
.hero{position:absolute;left:0;top:14px;width:1200px;height:457px;
  background:radial-gradient(ellipse at 70% 30%,#7e5d10 0%,var(--hero) 45%,var(--hero-dark) 100%)}
.hero-deco{position:absolute;left:705px;top:70px;font:700 210px/1 Oswald,sans-serif;color:rgba(255,230,170,.07);letter-spacing:-6px}
.logo{position:absolute;left:183px;top:18px;color:var(--cream)}
.logo-name{font:400 52px/1 Comfortaa,sans-serif;letter-spacing:1px}
.logo-tag{position:absolute;left:84px;top:60px;white-space:nowrap;font:400 19px/1 Comfortaa,sans-serif;color:var(--gold)}
.nav{position:absolute;left:517px;top:14px;display:flex;list-style:none}
.nav a{display:block;height:78px;padding:29px 12px 0;font:700 14px/1 Oswald,sans-serif;color:#fff;text-decoration:none;text-transform:uppercase}
.nav .active a{background:var(--topbar);color:var(--orange)}
.portrait{position:absolute;left:176px;top:121px;width:342px;height:342px;border-radius:50%;
  background:#f7f7f7;box-shadow:0 0 0 4px #fff,0 6px 16px rgba(0,0,0,.35)}
.portrait-photo{position:absolute;left:6px;top:6px;width:330px;height:330px;border-radius:50%;
  background:radial-gradient(circle at 45% 45%,#8a8a8a 0%,#3d3d3d 60%,#cfcfcf 100%)}
.intro{position:absolute;left:548px;top:190px;font-family:"Black Ops One",sans-serif;line-height:1}
.intro-lead{font-size:33px;color:#fff}
.intro-name{font-size:74px;color:var(--gold);margin-top:2px;letter-spacing:-1px}
.intro-role{font-size:36px;color:#fff;margin-top:4px}
.film-button{position:absolute;left:548px;top:357px;width:258px;height:68px}
.film-button span{position:absolute;left:0;top:0;width:258px;height:68px;display:flex;align-items:center;justify-content:center;
  font:400 25px/1 "Black Ops One",sans-serif;color:#111;text-decoration:none}
.camera{position:absolute;left:792px;top:346px;width:200px;height:142px;border-radius:18px;
  background:linear-gradient(160deg,#3a3a3a,#0e0e0e);box-shadow:0 0 0 5px #fff}
.lower{position:absolute;left:0;top:471px;width:1200px;height:241px;
  background:repeating-linear-gradient(115deg,#1a1a1a 0 2px,#222 2px 4px)}
.reel-icon{position:absolute;left:188px;top:497px}
.script{font-family:"Nothing You Could Do",cursive;color:#eee}
.releases-title{position:absolute;left:252px;top:503px;font-size:27px}
.releases-arrow{position:absolute;left:482px;top:506px}
.slider-arrow{position:absolute;top:605px}
.thumb{position:absolute;top:584px;width:84px;height:84px;border-radius:50%}
.contact-label{position:absolute;left:793px;font-size:26px;color:#aaa}
.email{position:absolute;left:793px;top:556px;font:400 22px/1 Oswald,sans-serif;color:var(--orange);text-decoration:none;letter-spacing:.5px}
.social{position:absolute;top:664px;height:32px;border-radius:16px;background:#3a3a3a;
  font:400 18px/32px Oswald,sans-serif;color:#ddd;text-align:center;text-decoration:none}
.footer{position:absolute;left:0;top:712px;width:1200px;height:38px;background:var(--footer)}
.footer p{position:absolute;left:185px;top:15px;font:400 9px/1 Arimo,sans-serif;color:var(--muted)}
</style>
</head>
<body>
<div class="page">
  <div class="topbar"></div>
  <header class="hero">
    <div class="hero-deco" aria-hidden="true">HI</div>
  </header>

  <div class="logo">
    <div class="logo-name">karim</div>
    <div class="logo-tag">independent film maker</div>
  </div>

  <ul class="nav">
    <li class="active"><a href="#">Home</a></li>
    <li><a href="#">Biography</a></li>
    <li><a href="#">Recent Releases</a></li>
    <li><a href="#">Gallery</a></li>
    <li><a href="#">Awards</a></li>
    <li><a href="#">Contact</a></li>
  </ul>

  <div class="portrait">
    <div class="portrait-photo" role="img" aria-label="Black and white portrait photo of the film maker"></div>
  </div>

  <div class="intro">
    <div class="intro-lead">I AM</div>
    <div class="intro-name">KARIM</div>
    <div class="intro-role">CREATIVE FILM MAKER</div>
  </div>

  <a class="film-button" href="#">
    <svg width="258" height="68" viewBox="0 0 258 68" aria-hidden="true">
      <rect x="0" y="0" width="258" height="68" rx="4" fill="#d2d2d2"/>
      <g fill="#6a5010">
        <rect x="10" y="4" width="6" height="7" rx="1"/><rect x="26" y="4" width="6" height="7" rx="1"/><rect x="42" y="4" width="6" height="7" rx="1"/><rect x="58" y="4" width="6" height="7" rx="1"/><rect x="74" y="4" width="6" height="7" rx="1"/><rect x="90" y="4" width="6" height="7" rx="1"/><rect x="106" y="4" width="6" height="7" rx="1"/><rect x="122" y="4" width="6" height="7" rx="1"/><rect x="138" y="4" width="6" height="7" rx="1"/><rect x="154" y="4" width="6" height="7" rx="1"/><rect x="170" y="4" width="6" height="7" rx="1"/><rect x="186" y="4" width="6" height="7" rx="1"/><rect x="202" y="4" width="6" height="7" rx="1"/><rect x="218" y="4" width="6" height="7" rx="1"/><rect x="234" y="4" width="6" height="7" rx="1"/>
        <rect x="10" y="57" width="6" height="7" rx="1"/><rect x="26" y="57" width="6" height="7" rx="1"/><rect x="42" y="57" width="6" height="7" rx="1"/><rect x="58" y="57" width="6" height="7" rx="1"/><rect x="74" y="57" width="6" height="7" rx="1"/><rect x="90" y="57" width="6" height="7" rx="1"/><rect x="106" y="57" width="6" height="7" rx="1"/><rect x="122" y="57" width="6" height="7" rx="1"/><rect x="138" y="57" width="6" height="7" rx="1"/><rect x="154" y="57" width="6" height="7" rx="1"/><rect x="170" y="57" width="6" height="7" rx="1"/><rect x="186" y="57" width="6" height="7" rx="1"/><rect x="202" y="57" width="6" height="7" rx="1"/><rect x="218" y="57" width="6" height="7" rx="1"/><rect x="234" y="57" width="6" height="7" rx="1"/>
      </g>
    </svg>
    <span>READ ABOUT ME</span>
  </a>

  <div class="camera" role="img" aria-label="Professional video camera"></div>

  <section class="lower">
  </section>

  <svg class="reel-icon" width="52" height="52" viewBox="0 0 52 52" aria-hidden="true">
    <circle cx="26" cy="26" r="25" fill="#cfcfcf"/>
    <circle cx="26" cy="26" r="21" fill="#e9e9e9"/>
    <g fill="#444">
      <circle cx="26" cy="13" r="6"/><circle cx="38" cy="22" r="6"/><circle cx="33" cy="37" r="6"/><circle cx="19" cy="37" r="6"/><circle cx="14" cy="22" r="6"/>
      <circle cx="26" cy="26" r="2.5"/>
    </g>
  </svg>
  <div class="releases-title script">View My Latest Releases</div>
  <svg class="releases-arrow" width="50" height="46" viewBox="0 0 50 46" aria-hidden="true">
    <path d="M2 6 C28 0 46 14 44 40" fill="none" stroke="#eee" stroke-width="1.6"/>
    <path d="M36 33 L44 41 L49 31" fill="none" stroke="#eee" stroke-width="1.6"/>
  </svg>

  <svg class="slider-arrow" style="left:194px" width="24" height="44" viewBox="0 0 24 44" aria-hidden="true"><path d="M22 1 L2 22 L22 43" fill="none" stroke="#ddd" stroke-width="1.5"/></svg>
  <div class="thumb" style="left:229px;background:linear-gradient(135deg,#6f7a6a,#2b2a2a 60%,#8d2b2b)" role="img" aria-label="Film still: two people talking outdoors"></div>
  <div class="thumb" style="left:338px;background:linear-gradient(135deg,#4c6a2a,#6b5a3a 60%,#2c3a1e)" role="img" aria-label="Film still: two people seated in a forest"></div>
  <div class="thumb" style="left:445px;background:radial-gradient(circle,#a8773c,#e4c9a0 80%)" role="img" aria-label="Film still: costumed warrior in a desert"></div>
  <div class="thumb" style="left:551px;background:linear-gradient(135deg,#6a5a4a,#2d3040 60%,#b69a74)" role="img" aria-label="Film still: men in suits in an office"></div>
  <svg class="slider-arrow" style="left:646px" width="24" height="44" viewBox="0 0 24 44" aria-hidden="true"><path d="M2 1 L22 22 L2 43" fill="none" stroke="#ddd" stroke-width="1.5"/></svg>

  <div class="contact-label script" style="top:505px">Please Write me at</div>
  <a class="email" href="mailto:reachme@karimreels.com">reachme@karimreels.com</a>
  <div class="contact-label script" style="top:610px">Follow Me On</div>
  <a class="social" href="#" style="left:792px;width:76px">linkbook</a>
  <a class="social" href="#" style="left:882px;width:76px">chatter</a>

  <footer class="footer">
    <p>copyright 2012. All Rights Reserved by Karim</p>
  </footer>
</div>
</body>
</html>
```